Plakat-Design für Vogelvolieren
Zielgruppe
Es geht um vier Din A4-Plakate, die an vier Vogelvolieren hängen und Informationen zu den Vögeln bieten, die sich in den Volieren befinden.
Die Volieren gehören zum Wildpark Kernbachtal. Einem kleinen Wildpark, bei dem ausschließlich Ehrenamtliche tätig sind. Der Eintritt ist frei.
Die Zielgruppe sind die Besucher - von klein bis groß, von jung bis alt
Aufgabenstellung
Gute Lesbarkeit, denn die Informationsvermittlung soll im Vordergrund stehen.
Wir benötigen 1 Plakatdesign und die offenen Daten in InDesign, denn dann würden wir bei den weiteren drei Plakaten die Texte und Fotos austauschen.
Es sind 2 Plakate mit 4 Vögeln und 2 Plakate mit 2 Vögeln.

```html
<!DOCTYPE html>
<html lang="de">
<head>
<meta charset="utf-8">
<title>Vogelvolieren – Wildpark Kernbachtal</title>
<link rel="stylesheet" href="https://fonts.googleapis.com/css2?family=Asap+Condensed:wght@400;500;600&family=Crimson+Pro:wght@600&display=swap">
<style>
  :root {
    --purple: #8a2468;
    --orange: #d2913f;
    --green: #5f9e55;
    --paper: #f4f4f3;
    --ink: #1f1d1c;
    --stage: #e4e4e4;
  }
  * { box-sizing: border-box; margin: 0; padding: 0; }
  html, body { width: 1200px; height: 1200px; overflow: hidden; background: var(--stage); }
  body { font-family: "Asap Condensed", sans-serif; color: var(--ink); }

  .poster {
    position: absolute; left: 190px; top: 20px;
    width: 820px; height: 1160px;
    display: grid; grid-template-columns: 410px 410px; grid-template-rows: 580px 580px;
    background: var(--paper);
  }
  .panel { position: relative; overflow: hidden; background: var(--paper); }
  .panel-art { position: absolute; inset: 0; width: 410px; height: 580px; }

  .brand {
    position: absolute; top: 14px; right: 10px;
    display: flex; align-items: center; gap: 5px;
    font-size: 10.5px; font-weight: 600; color: var(--purple); line-height: 1.1;
  }
  .brand-dot { width: 14px; height: 14px; border-radius: 50%; background: var(--purple); flex: none; }

  .title {
    position: absolute;
    background: var(--purple); color: #fff;
    font-family: "Crimson Pro", serif; font-weight: 600;
    font-size: 23px; line-height: 1.15; text-align: center; letter-spacing: 0.3px;
    border-radius: 30px 18px 34px 14px / 22px 30px 20px 28px;
    display: flex; align-items: center; justify-content: center;
  }

  .col { position: absolute; text-align: center; font-size: 12px; line-height: 17px; font-weight: 500; }
  .col p + p { margin-top: 8px; }
  .col-look { left: 8px; width: 204px; top: 285px; }
  .col-range { left: 244px; width: 152px; top: 343px; }
  .heading {
    color: var(--purple); font-size: 15.5px; font-weight: 600;
    text-decoration: underline; text-underline-offset: 2px; margin-bottom: 8px;
  }
  .fact { color: var(--green); }
  .map {
    display: block; width: 104px; height: 54px; margin: 0 auto 12px;
    background: linear-gradient(120deg, var(--green) 0 55%, var(--purple) 55% 68%, var(--green) 68%);
    border-radius: 10px 22px 12px 18px;
  }
  .marker { width: 22px; height: 22px; border-radius: 50%; background: var(--orange); margin: 10px auto 0; }
  .fact-wide { position: absolute; left: 0; right: 0; bottom: 12px; text-align: center; font-size: 12px; font-weight: 500; }
</style>
</head>
<body>
<main class="poster">

  <!-- Unzertrennliche -->
  <section class="panel">
    <svg class="panel-art" viewBox="0 0 410 580" aria-hidden="false">
      <defs>
        <linearGradient id="g-love" x1="0" y1="0" x2="1" y2="1">
          <stop offset="0" stop-color="#c39455"/><stop offset="1" stop-color="#d7b07a"/>
        </linearGradient>
      </defs>
      <path role="img" aria-label="Foto: Unzertrennliche auf einem Ast vor Holzwand" fill="url(#g-love)"
        d="M0,0 H410 V284 C380,296 360,312 333,312 C250,312 160,256 75,256 C45,256 20,275 0,291 Z"/>
      <path fill="var(--orange)" d="M0,291 C20,275 45,256 75,256 C120,256 160,268 205,284 C160,274 120,268 82,272 C45,276 20,292 0,306 Z"/>
      <path fill="var(--green)" d="M140,262 C200,278 260,312 333,312 C360,312 380,296 410,284 V298 C385,314 360,326 330,326 C258,326 200,292 140,262 Z"/>
      <path fill="var(--orange)" d="M246,0 C278,24 292,44 336,54 C368,60 394,62 410,68 V62 C392,56 370,52 340,46 C300,38 290,20 262,0 Z"/>
      <path fill="var(--paper)" d="M262,0 C290,20 300,38 340,46 C370,52 392,56 410,62 V0 Z"/>
    </svg>
    <div class="brand"><span class="brand-dot"></span>Wildpark<br>Kernbachtal</div>
    <h2 class="title" style="left:4px; top:205px; width:196px; height:46px;">Unzertrennliche</h2>
    <div class="col col-look">
      <h3 class="heading">Aussehen:</h3>
      <p>Ihre Farbgebung gibt den verschiedenen Arten ihren Namen. Es gibt Grauköpfchen, Orangeköpfchen, Tarantapapageien, Grünköpfchen, Rosenköpfchen, Pfirsichköpfchen, Schwarzköpfchen, Erdbeerköpfchen und Rußköpfchen.</p>
      <p>Unzertrennliche werden rund 13 bis 18 Zentimeter lang und wiegen etwa 50 Gramm.</p>
      <p class="fact" style="margin-top:16px;">Wussten Sie, das Unzertrennliche im Englischen „Lovebirds“ (übersetzt: „Liebesvögel“) heißen?</p>
    </div>
    <div class="col col-range">
      <h3 class="heading">Vorkommen:</h3>
      <span class="map" role="img" aria-label="Weltkarte mit markiertem Verbreitungsgebiet in Afrika"></span>
      <p>Unzertrennliche leben in Afrika sowohl in heißen Savannen als auch in feucht-tropischen Regenwäldern.</p>
      <div class="marker"></div>
    </div>
  </section>

  <!-- Zebrafinken -->
  <section class="panel">
    <svg class="panel-art" viewBox="0 0 410 580">
      <defs>
        <linearGradient id="g-zebra" x1="0" y1="0" x2="1" y2="1">
          <stop offset="0" stop-color="#c7a468"/><stop offset="1" stop-color="#dcc08a"/>
        </linearGradient>
      </defs>
      <path role="img" aria-label="Foto: Zebrafink auf einem Bambusstab" fill="url(#g-zebra)"
        d="M0,0 H410 V284 C380,296 360,312 333,312 C250,312 160,256 75,256 C45,256 20,275 0,291 Z"/>
      <path fill="var(--orange)" d="M0,291 C20,275 45,256 75,256 C120,256 160,268 205,284 C160,274 120,268 82,272 C45,276 20,292 0,306 Z"/>
      <path fill="var(--green)" d="M140,262 C200,278 260,312 333,312 C360,312 380,296 410,284 V298 C385,314 360,326 330,326 C258,326 200,292 140,262 Z"/>
      <path fill="var(--orange)" d="M246,0 C278,24 292,44 336,54 C368,60 394,62 410,68 V62 C392,56 370,52 340,46 C300,38 290,20 262,0 Z"/>
      <path fill="var(--paper)" d="M262,0 C290,20 300,38 340,46 C370,52 392,56 410,62 V0 Z"/>
    </svg>
    <div class="brand"><span class="brand-dot"></span>Wildpark<br>Kernbachtal</div>
    <h2 class="title" style="left:248px; top:196px; width:158px; height:84px;">Australische<br>Zebrafinken</h2>
    <div class="col col-look">
      <h3 class="heading">Aussehen:</h3>
      <p>Gut zu erkennen sind Zebrafinken an ihrem orange-roten Schnabel, am schwarzen Tränenstrich unter den Augen und der schwarzen Zebra-Musterung der Brust. Das Gefieder der Männchen, die über einen orange-farbenen Wangenfleck verfügen, ist kräftiger als das der Weibchen. Ihre kurzen, eckigen Flügel machen Zebrafinken zu wahren Flugakrobaten.</p>
      <p>Zebrafinken werden rund 12 Zentimeter lang und wiegen 12 bis 14 Gramm.</p>
    </div>
    <div class="col col-range">
      <h3 class="heading">Vorkommen:</h3>
      <span class="map" role="img" aria-label="Weltkarte mit markiertem Verbreitungsgebiet in Australien"></span>
      <p>Australische Zebrafinken leben fast überall in Australien.</p>
      <p class="fact" style="margin-top:24px;">Lorem ipsum dolor sit amet, consetetur sadipscing elitr, sed diam</p>
    </div>
  </section>

  <!-- Wachteln -->
  <section class="panel">
    <svg class="panel-art" viewBox="0 0 410 580">
      <defs>
        <linearGradient id="g-quail" x1="0" y1="0" x2="0" y2="1">
          <stop offset="0" stop-color="#bf9a66"/><stop offset="0.35" stop-color="#8d877c"/><stop offset="1" stop-color="#a79a86"/>
        </linearGradient>
      </defs>
      <path role="img" aria-label="Foto: Europäische Wachtel auf Sandboden" fill="url(#g-quail)"
        d="M0,0 H410 V284 C380,296 360,312 333,312 C250,312 160,256 75,256 C45,256 20,275 0,291 Z"/>
      <path fill="var(--orange)" d="M0,291 C20,275 45,256 75,256 C120,256 160,268 205,284 C160,274 120,268 82,272 C45,276 20,292 0,306 Z"/>
      <path fill="var(--green)" d="M140,262 C200,278 260,312 333,312 C360,312 380,296 410,284 V298 C385,314 360,326 330,326 C258,326 200,292 140,262 Z"/>
      <path fill="var(--orange)" d="M246,0 C278,24 292,44 336,54 C368,60 394,62 410,68 V62 C392,56 370,52 340,46 C300,38 290,20 262,0 Z"/>
      <path fill="var(--paper)" d="M262,0 C290,20 300,38 340,46 C370,52 392,56 410,62 V0 Z"/>
    </svg>
    <div class="brand"><span class="brand-dot"></span>Wildpark<br>Kernbachtal</div>
    <h2 class="title" style="left:218px; top:198px; width:178px; height:90px;">Europäische<br>Wachteln</h2>
    <div class="col col-look">
      <h3 class="heading">Aussehen:</h3>
      <p>Europäische Wachteln, die auch als Feldwachteln bezeichnet werden, haben eine graubraune Gesamtfärbung mit einer Vielzahl rotbrauner und schwarzer Striche. Die Flügel sind grau. Die Augenfarbe ist rotbraun und damit ein Unterscheidungsmerkmal, denn die japanischen Zuchtwachteln haben dunkle Augen.</p>
      <p>Wachteln wiegen rund 90 bis 100 Gramm.</p>
    </div>
    <div class="col col-range">
      <h3 class="heading">Vorkommen:</h3>
      <span class="map" role="img" aria-label="Weltkarte mit markiertem Verbreitungsgebiet in Europa, Westasien und Afrika"></span>
      <p>Europäische Wachteln leben in fast ganz Europa, den westlichen Teil Asiens und einem großen Teil Afrikas.</p>
    </div>
    <p class="fact fact-wide">Lorem ipsum dolor sit amet, consetetur sadipscing elitr, sed diam</p>
  </section>

  <!-- Katharinasittiche -->
  <section class="panel">
    <svg class="panel-art" viewBox="0 0 410 580">
      <defs>
        <linearGradient id="g-parakeet" x1="0" y1="0" x2="1" y2="1">
          <stop offset="0" stop-color="#8f7a5f"/><stop offset="0.5" stop-color="#9aa08e"/><stop offset="1" stop-color="#7d806f"/>
        </linearGradient>
      </defs>
      <path role="img" aria-label="Foto: Sittich mit gelbem Schopf auf einem Futternapf in der Voliere" fill="url(#g-parakeet)"
        d="M0,0 H410 V284 C380,296 360,312 333,312 C250,312 160,256 75,256 C45,256 20,275 0,291 Z"/>
      <path fill="var(--orange)" d="M0,291 C20,275 45,256 75,256 C120,256 160,268 205,284 C160,274 120,268 82,272 C45,276 20,292 0,306 Z"/>
      <path fill="var(--green)" d="M140,262 C200,278 260,312 333,312 C360,312 380,296 410,284 V298 C385,314 360,326 330,326 C258,326 200,292 140,262 Z"/>
      <path fill="var(--orange)" d="M246,0 C278,24 292,44 336,54 C368,60 394,62 410,68 V62 C392,56 370,52 340,46 C300,38 290,20 262,0 Z"/>
      <path fill="var(--paper)" d="M262,0 C290,20 300,38 340,46 C370,52 392,56 410,62 V0 Z"/>
    </svg>
    <div class="brand"><span class="brand-dot"></span>Wildpark<br>Kernbachtal</div>
    <h2 class="title" style="left:3px; top:10px; width:208px; height:70px;">Katharinasittiche</h2>
    <div class="col col-look">
      <h3 class="heading">Aussehen:</h3>
      <p>Mit ihrem leuchtend grünen Gefieder mit blauschwarzen Abzeichen sind Katharinasittiche perfekt an die Wälder in ihrer Heimat angepasst. Aufgrund von gezielten Züchtungen gibt es mittlerweile auch gelbe, blaue, türkis- und creme-farbene Katharinasittiche. Männliche und weibliche Katharinasittiche lassen sich äußerlich kaum unterscheiden.</p>
      <p>Erwachsene Vögel werden 16 bis 17 Zentimeter lang, wobei der Schwanz rund 6 Zentimeter misst, und wiegen etwa 50 bis 60 Gramm.</p>
    </div>
    <div class="col col-range">
      <h3 class="heading">Vorkommen:</h3>
      <span class="map" role="img" aria-label="Weltkarte mit markiertem Verbreitungsgebiet in Mittel- und Südamerika"></span>
      <p>Katharinasittiche leben in Mittel- und Südamerika.</p>
      <p class="fact" style="margin-top:24px;">Lorem ipsum dolor sit amet, consetetur sadipscing elitr, sed diam nonumy eirmod tempor</p>
    </div>
  </section>

</main>
</body>
</html>
```